Frischer, moderner, emotionaler Baumarkt-Onlineshop sucht passende Außendarstellung
Zielgruppe
Wir sind gerade im Aufbau eines Onlinebaumarktes. In diesem Baumarkt bekommt man vom Nagel bis hin zum neuen Fußboden alles was das Herz begehrt. Wir möchten der Begleiter für jeden Heimwerker sein, der eine gute Beratung, hochwertige Produkte und einen aufgeräumten Fachhandel sucht. Wir wollen einen emotionalen Onlineshop schaffen, bei dem das richtige Produkt dich sucht und nicht du stundenlang das richtige Produkt.
Aufgabenstellung
Wir möchten ein modernes und frisches Bild, der etwas eingestaubten Baumarktlandschaft vermitteln. Bei uns soll es Spaß machen, nach tollen Produkten zu stöbern. Der Kunde soll visuell angesprochen werden und sich intuitiv auf unseren Seiten bewegen können. Wenn man sich die gängigen Shopseiten anschaut, hat man eine ewig lange Navigation um zu seinem Produkt zu kommen. Wir möchten diesen Prozess, durch intelligente Filter gerne verkürzen, so dass jeder Laie sein Produkt ganz leicht findet.
Die Farben der Seite sollten sich an das Logo anlehnen oder diese auch einfließen lassen, damit die Seite wie aus einem Guss wirkt. Interessieren würde uns auch wie die Seite nicht nur auf dem Desktop aussieht, sondern auch seine Übersichtigkeit auf einem Tablet oder Smartphone beibehält.

```html
<!DOCTYPE html>
<html lang="de">
<head>
<meta charset="utf-8">
<title>werkhaus-online.de – Badezimmer</title>
<link rel="stylesheet" href="https://fonts.googleapis.com/css2?family=Open+Sans:wght@400;600;700&family=Oswald:wght@400;500&display=swap">
<style>
:root{
  --green:#8cbf26;
  --green-dark:#76a81c;
  --blue:#1f3a8f;
  --blue-soft:#dde3fb;
  --price:#7cb526;
  --sale:#c4161c;
  --ink:#222;
  --muted:#8a8a8a;
  --line:#e2e2e2;
  --panel:#f3f3f3;
  --footer:#e7eaf3;
  --white:#fff;
}
*{box-sizing:border-box;margin:0;padding:0}
html,body{width:1200px;height:962px;overflow:hidden}
body{background:var(--white);font-family:"Open Sans",Arial,sans-serif;color:var(--ink);position:relative}

/* header */
.site-header{position:absolute;top:0;left:0;width:1200px;height:100px;border-bottom:2px solid #e6e6e6}
.brand{position:absolute;left:167px;top:46px;display:flex;align-items:center;gap:8px;font-weight:700;font-size:19px;line-height:24px;color:var(--blue);letter-spacing:-.3px;white-space:nowrap;max-width:215px}
.brand-mark{width:13px;height:13px;background:var(--blue);flex:none}
.search{position:absolute;left:420px;top:48px;width:208px;height:24px;border:1px solid #ccc;border-radius:2px;font-size:10px;color:#666;padding:5px 8px}
.search svg{position:absolute;right:6px;top:5px}
.top-nav{position:absolute;left:715px;top:0;height:24px;display:flex;border:1px solid var(--line);border-top:none;font-size:10px;font-weight:600;color:#555}
.top-nav span{padding:5px 8px;border-right:1px solid var(--line);white-space:nowrap}
.top-nav span:last-child{border:none}
.top-nav .off{color:#aaa;font-weight:400;padding:0}
.cart{position:absolute;left:848px;top:44px;width:190px}
.cart-title{font-size:11px;font-weight:700;color:#555;letter-spacing:.3px}
.cart-sum{position:absolute;left:110px;top:1px;font-size:9px;color:#e4572e}
.cart-select{margin-top:5px;width:120px;height:17px;border:1px solid var(--line);font-size:8px;color:#aaa;padding:2px 6px;white-space:nowrap}
.cart svg{position:absolute;left:136px;top:-8px}

/* main */
.main{position:absolute;top:102px;left:167px;width:871px;height:498px;background:var(--green)}
.sidebar{position:absolute;left:0;top:0;width:162px}
.cat-title{margin-top:7px;background:var(--blue);color:var(--white);font-size:27px;font-weight:400;line-height:26px;padding:6px 15px 4px;height:62px}
.cat-list{list-style:none;background:var(--white);margin-top:10px;border:2px solid var(--panel)}
.cat-list li{font-size:9px;font-weight:600;height:31.5px;padding:9px 6px;border-bottom:1px solid var(--line);display:flex;justify-content:space-between;align-items:center;white-space:nowrap}
.cat-list li.active{background:var(--blue-soft);color:var(--blue)}
.cat-list li svg{flex:none}
.trust{background:var(--white);margin-top:10px;height:60px;display:flex;align-items:center;gap:8px;padding:0 4px}
.trust-badge{width:44px;height:44px;border-radius:50%;background:#2a2a2a;border:3px solid #777;flex:none}
.trust p{font-size:10px;line-height:13px;color:var(--muted)}
.trust b{color:var(--ink);font-weight:600}
.info{background:var(--white);margin-top:10px;height:110px}
.info h3{background:var(--panel);font-family:"Oswald",sans-serif;font-weight:500;font-size:12px;padding:9px 11px;color:#333}
.info ul{list-style:none;padding:8px 7px;font-size:9px;color:var(--muted);line-height:20px}

.content{position:absolute;left:170px;top:0;width:701px}
.toolbar{background:var(--panel);margin-top:7px;height:63px;padding:9px 12px;font-size:10px;font-weight:700;color:#333}
.tb-row{display:flex;align-items:center;height:22px;margin-bottom:8px;white-space:nowrap}
.select{display:inline-flex;align-items:center;border:1px solid #ddd;background:var(--white);height:19px;font-weight:400;color:#888;font-size:9px;padding-left:8px;margin-left:6px}
.select i{display:block;width:18px;height:19px;background:var(--green);margin-left:8px}
.view{margin-left:auto;display:flex;align-items:center;gap:6px}
.view b{display:block;width:22px;height:16px;border:1px solid #ccc}
.view b.on{background:#333}
.perpage{margin-left:auto;display:flex;align-items:center}
.pager{display:inline-flex;gap:4px;margin-left:16px}
.pager span{width:16px;height:16px;border:1px solid #ccc;background:var(--white);font-size:8px;font-weight:400;display:grid;place-items:center}
.pager span.on{background:#888;color:#fff;border-color:#888}
.page-info{margin-left:auto;font-weight:400}
.page-info b{font-weight:700}

.grid{display:grid;grid-template-columns:repeat(4,1fr);gap:10px;margin-top:10px}
.card{background:var(--white);height:292px;padding:10px 12px;position:relative}
.card.partial{height:120px}
.sale-tag{position:absolute;left:0;top:20px;width:20px;height:22px;background:var(--sale);color:#fff;font-weight:700;font-size:12px;display:grid;place-items:center}
.photo{height:80px;width:90px;margin:8px auto 0;border-radius:4px}
.photo.white{background:linear-gradient(#fafafa,#e0e0e0)}
.photo.wood{background:linear-gradient(#c9823f,#8f5220)}
.title{font-family:"Oswald",sans-serif;font-weight:400;font-size:11.5px;text-transform:uppercase;margin-top:22px;letter-spacing:-.2px;white-space:nowrap}
.desc{font-size:8.5px;color:var(--muted);line-height:11.5px;margin-top:4px;height:34px;overflow:hidden}
.old{font-size:7.5px;color:var(--muted);text-decoration:line-through;margin-top:8px}
.price{font-size:11px;font-weight:700;color:var(--price);margin-top:4px}
.price.sale{color:var(--sale);margin-top:1px}
.actions{position:absolute;left:12px;right:12px;bottom:12px}
.btn{display:flex;justify-content:space-between;align-items:center;font-size:10px;color:#777;background:var(--panel);height:17px;padding:0 5px;margin-top:4px}
.btn.go{background:#111;color:#fff;font-weight:600}
.btn.go.hot{background:var(--green)}

/* chat tab */
.chat{position:absolute;left:0;top:231px;width:57px;height:218px;background:var(--green);color:#fff}
.chat-close{position:absolute;left:5px;top:5px;width:15px;height:15px;background:#fff;display:grid;place-items:center}
.chat-text{position:absolute;left:12px;bottom:14px;transform-origin:left bottom;transform:rotate(-90deg) translateY(100%);white-space:nowrap;width:175px}
.chat-text strong{display:block;font-size:19px;line-height:22px}
.chat-text small{font-size:9px}

/* footer */
.site-footer{position:absolute;top:606px;left:0;width:1200px;height:356px;background:var(--footer);border-top:2px solid #d8dcea}
.foot-cols{position:absolute;left:167px;top:0;width:871px;display:grid;grid-template-columns:178px 190px 188px 1fr;height:130px}
.foot-col{border-left:1px solid #c9cdd9;padding:12px 0 0 28px;font-size:8px;line-height:11.5px;color:#333}
.foot-col:last-child{border-right:1px solid #c9cdd9}
.foot-col h4{font-size:10px;color:var(--blue);font-weight:700;margin-bottom:6px}
.hotline{font-size:14px;font-weight:700;margin-top:10px;line-height:14px}
.news-field{margin-top:20px;width:162px;height:17px;border:1px solid #aab;background:#fff;font-size:7px;padding:3px 4px;position:relative}
.news-field i{position:absolute;right:-1px;top:-1px;width:17px;height:17px;background:var(--blue)}
</style>
</head>
<body>

<header class="site-header">
  <div class="brand"><span class="brand-mark"></span>werkhaus-online.de</div>
  <div class="search">Suche:
    <svg width="12" height="12" viewBox="0 0 12 12"><circle cx="5" cy="5" r="3.8" fill="none" stroke="#333" stroke-width="1.4"/><line x1="8" y1="8" x2="11" y2="11" stroke="#333" stroke-width="1.6"/></svg>
  </div>
  <nav class="top-nav"><span>Mein Konto</span><span>Merkzettel</span><span>Service/Hilfe ⌄</span><span>EUR <span class="off">USD</span></span></nav>
  <div class="cart">
    <div class="cart-title">WARENKORB</div>
    <div class="cart-sum">0,00</div>
    <div class="cart-select">Positionen anzeigen</div>
    <svg width="42" height="44" viewBox="0 0 42 44"><g fill="none" stroke="#888" stroke-width="1.5"><path d="M6 2v30h32M14 2v30"/><rect x="8" y="18" width="28" height="12"/></g><circle cx="10" cy="38" r="3" fill="#777"/><circle cx="34" cy="38" r="3" fill="#777"/></svg>
  </div>
</header>

<aside class="chat">
  <div class="chat-close"><svg width="9" height="9" viewBox="0 0 9 9"><path d="M1 1l7 7M8 1l-7 7" stroke="#111" stroke-width="1.6"/></svg></div>
  <div class="chat-text"><strong>LIVE-Beratung</strong><small>Wir beraten Sie kostenlos im Chat</small></div>
</aside>

<main class="main">
  <div class="sidebar">
    <h1 class="cat-title">Bade-<br>zimmer</h1>
    <ul class="cat-list">
      <li>Armaturen<svg width="9" height="6" viewBox="0 0 9 6"><path d="M1 1l3.5 3.5L8 1" fill="none" stroke="#888"/></svg></li>
      <li>Badaccessoires<svg width="9" height="6" viewBox="0 0 9 6"><path d="M1 1l3.5 3.5L8 1" fill="none" stroke="#888"/></svg></li>
      <li>Badewannen<svg width="9" height="6" viewBox="0 0 9 6"><path d="M1 1l3.5 3.5L8 1" fill="none" stroke="#888"/></svg></li>
      <li>Badkeramik<svg width="9" height="6" viewBox="0 0 9 6"><path d="M1 1l3.5 3.5L8 1" fill="none" stroke="#888"/></svg></li>
      <li class="active">Badmöbel<svg width="9" height="6" viewBox="0 0 9 6"><path d="M1 1l3.5 3.5L8 1" fill="none" stroke="#1f3a8f"/></svg></li>
      <li>Brause &amp; Duschzubehör<svg width="9" height="6" viewBox="0 0 9 6"><path d="M1 1l3.5 3.5L8 1" fill="none" stroke="#888"/></svg></li>
      <li>Heizgeräte<svg width="9" height="6" viewBox="0 0 9 6"><path d="M1 1l3.5 3.5L8 1" fill="none" stroke="#888"/></svg></li>
    </ul>
    <div class="trust">
      <span class="trust-badge"></span>
      <p><b>Sicher</b> einkaufen<br>Geprüfter Shop<br>zertifiziert</p>
    </div>
    <div class="info">
      <h3>INFORMATIONEN</h3>
      <ul><li>Hilfe / Support</li><li>Über uns</li><li>Kontakt</li></ul>
    </div>
  </div>

  <section class="content">
    <div class="toolbar">
      <div class="tb-row">Sortierung: <span class="select">Erscheinungsdatum<i></i></span>
        <span class="view">Ansicht: <b class="on"></b><b></b></span>
        <span class="perpage">Artikel pro Seite: <span class="select">12<i></i></span></span>
      </div>
      <div class="tb-row">Blättern: <span class="pager"><span class="on">1</span><span>2</span><span>›</span></span>
        <span class="page-info">Seite <b>1</b> von <b>2</b></span>
      </div>
    </div>

    <div class="grid">
      <article class="card">
        <span class="sale-tag">%</span>
        <div class="photo white" role="img" aria-label="Produktfoto: weißer Schlüsselkasten"></div>
        <h2 class="title">Schlüsselkasten</h2>
        <p class="desc">Diu se Quater rare passim dens, sui hac obscoena...</p>
        <p class="old">Statt: 79,00 € *</p>
        <p class="price sale">69,99 € *</p>
        <div class="actions"><div class="btn">Jetzt bestellen<span>›</span></div><div class="btn">Vergleichen<span>›</span></div><div class="btn go">Zum Produkt<span>➜</span></div></div>
      </article>
      <article class="card">
        <div class="photo wood" role="img" aria-label="Produktfoto: Holzstuhl mit gekreuzter Lehne"></div>
        <h2 class="title">Versandkosten nach Gewicht</h2>
        <p class="desc">Curvo escendo adsum per Frutex, ubi alt animadverto...</p>
        <p class="price">74,99 € *</p>
        <div class="actions"><div class="btn">Jetzt bestellen<span>›</span></div><div class="btn">Vergleichen<span>›</span></div><div class="btn go hot">Zum Produkt<span>➜</span></div></div>
      </article>
      <article class="card">
        <div class="photo white" role="img" aria-label="Produktfoto: eckiger weißer Couchtisch"></div>
        <h2 class="title">Couchtisch eckig weiss</h2>
        <p class="desc">Inhumanitas enim ars ara Noxa tunc aqua refrigerium...</p>
        <p class="price">329,99 € *</p>
        <div class="actions"><div class="btn">Jetzt bestellen<span>›</span></div><div class="btn">Vergleichen<span>›</span></div><div class="btn go">Zum Produkt<span>➜</span></div></div>
      </article>
      <article class="card">
        <div class="photo wood" role="img" aria-label="Produktfoto: runder brauner Couchtisch"></div>
        <h2 class="title">Couchtisch rund braun</h2>
        <p class="desc">Subdo qui Gemo ipse somniculosus. Non Apertio ops, per...</p>
        <p class="price">349,99 € *</p>
        <div class="actions"><div class="btn">Jetzt bestellen<span>›</span></div><div class="btn">Vergleichen<span>›</span></div><div class="btn go">Zum Produkt<span>➜</span></div></div>
      </article>
      <article class="card partial"><div class="photo wood" role="img" aria-label="Produktfoto: Holzhocker mit drei Beinen"></div></article>
      <article class="card partial"><div class="photo wood" role="img" aria-label="Produktfoto: Holzstuhl mit gekreuzter Lehne"></div></article>
      <article class="card partial"><div class="photo white" role="img" aria-label="Produktfoto: weißer Wandspiegel mit Ablage"></div></article>
      <article class="card partial"><div class="photo white" role="img" aria-label="Produktfoto: weißes Badregal mit Schublade"></div></article>
    </div>
  </section>
</main>

<footer class="site-footer">
  <div class="foot-cols">
    <div class="foot-col"><h4>Service Hotline</h4>Telefonische Unterstützung und<br>Beratung unter:<div class="hotline">0800 - 246810</div>Mo-Fr, 09:00 - 17:00 Uhr</div>
    <div class="foot-col"><h4>Shop Service</h4>Defektes Produkt<br>Partnerprogramm<br>rechtliche Vorabinformationen<br>Kontakt<br>Versand und<br>Zahlungsbedingungen<br>Rückgabe</div>
    <div class="foot-col"><h4>Informationen</h4>Newsletter<br>Über uns<br>Datenschutz<br>Impressum</div>
    <div class="foot-col"><h4>Newsletter</h4>Abonnieren Sie den kostenlosen Werkhaus<br>Newsletter und verpassen Sie keine Neuigkeit<br>oder Aktion mehr aus dem Werkhaus.<div class="news-field">Ihre E-Mail Adresse<i></i></div></div>
  </div>
</footer>

</body>
</html>
```